Creative Stationary for Solo Law Firm

I am looking for stationary designs for my solo law firm called TM Halvorsen Law PLLC. My logo is attached. I'd like the logo incorporated into the design.

I'm looking for a stationary design that is a bit outside of the box and not too standard or boring. The final design should communicate professionalism.

Target Market(s)

United States Clients, Opposing Counsel

Industry/Entity Type

Legal

Font styles to use
Sans Serif

Requirements
Must have
• The stationary design must incorporate my logo design attached. The design itself must be creative. The envelope design must follow standard United States designs with room for the postage stamp at the top right corner and space for the recipient's address in the middle.

```html
<!DOCTYPE html>
<html lang="en">
<head>
<meta charset="utf-8">
<title>TM Halvorsen Law – Stationery</title>
<link rel="stylesheet" href="https://fonts.googleapis.com/css2?family=Questrial&display=swap">
<style>
:root{
  --bg:#262627;
  --paper:#f1f1f2;
  --folder:#cbcbcc;
  --folder-line:#b8b8ba;
  --navy:#0d1f5c;
  --grey-wave:#c9c9cb;
  --grey-wave-light:#dcdcde;
  --ink:#2a2a2a;
  --sig:#4a5fb0;
}
*{margin:0;padding:0;box-sizing:border-box}
html,body{width:1200px;height:1041px;overflow:hidden;background:var(--bg)}
body{position:relative;font-family:"Questrial",sans-serif;color:var(--ink)}
.piece{position:absolute;overflow:hidden}
.brand{position:absolute;color:var(--navy);font-family:"Questrial",sans-serif;font-weight:400;letter-spacing:.02em;white-space:nowrap}
.wave{position:absolute;left:0;bottom:0;width:100%;display:block}
.small{font-size:5.6px;line-height:7px;white-space:nowrap}

/* folder */
.folder{left:165px;top:76px;width:417px;height:541px;background:var(--folder);border-radius:4px}
.folder .spine{position:absolute;left:22px;top:0;width:4px;height:100%;border-left:1px solid var(--folder-line);border-right:1px solid var(--folder-line)}
.folder .brand{left:118px;top:76px;font-size:21px}

/* letterhead */
.letterhead{left:615px;top:94px;width:403px;height:523px;background:var(--paper)}
.letterhead .brand{left:37px;top:45px;font-size:14px}
.contact{position:absolute}
.contact li{list-style:none;display:flex;align-items:center;gap:3px}
.icon{display:inline-block;width:4.5px;height:4.5px;background:var(--ink);border-radius:1px}
.letterhead .contact{left:294px;top:34px}
.letter-body{position:absolute;left:37px;top:144px;width:330px;font-size:5.6px;line-height:7px;text-align:justify}
.letter-body p{margin-bottom:7px}
.letter-body .greeting{font-weight:700;margin-bottom:8px}
.signoff{position:absolute;left:37px;top:314px;font-size:5.6px;line-height:7px}
.signoff strong{display:block}
.signature{position:absolute;left:84px;top:310px;width:80px;height:30px;background:linear-gradient(90deg,rgba(74,95,176,.18),rgba(74,95,176,.06));border-radius:3px}

/* envelope front */
.envelope-front{left:132px;top:646px;width:450px;height:195px;background:var(--paper)}
.envelope-front .brand{left:24px;top:30px;font-size:14px}
.envelope-front .return{position:absolute;left:24px;top:58px}

/* envelope back */
.envelope-back{left:615px;top:646px;width:451px;height:195px;background:var(--paper)}
.envelope-back .flap{position:absolute;left:0;top:0;width:100%;height:66px}
.envelope-back .brand{left:0;width:100%;text-align:center;top:29px;font-size:11px}
.envelope-back .web{position:absolute;left:0;width:100%;text-align:center;top:172px}

/* cards */
.card-front{left:416px;top:870px;width:167px;height:95px;background:var(--folder)}
.card-front .brand{left:0;width:100%;text-align:center;top:40px;font-size:12px}
.card-back{left:615px;top:870px;width:167px;height:95px;background:var(--paper)}
.card-back .brand{left:17px;top:39px;font-size:8.5px}
.card-back .divider{position:absolute;left:90px;top:18px;width:1px;height:50px;background:#d2d2d4}
.card-back .details{position:absolute;left:98px;top:18px;font-size:4.2px;line-height:5.2px}
.card-back .name{color:var(--navy);font-weight:700;font-size:5.2px;letter-spacing:.04em}
.card-back .icon{width:3.4px;height:3.4px}
</style>
</head>
<body>

<section class="piece folder" aria-label="Presentation folder">
  <div class="spine"></div>
  <div class="brand">TM Halvorsen Law</div>
</section>

<section class="piece letterhead" aria-label="Letterhead">
  <div class="brand">TM Halvorsen Law</div>
  <ul class="contact small">
    <li><span class="icon"></span>555.210.4180</li>
    <li><span class="icon"></span>555.210.4190</li>
    <li><span class="icon"></span>www.tmhalvorsenlaw.com</li>
    <li>218 N. Harbor Blvd, Suite B</li>
    <li>Fullerton CA 92832</li>
  </ul>
  <div class="letter-body">
    <p class="greeting">Dear sir,</p>
    <p>Communication is a very integral part of living creatures, animals and humans. Communication may be verbal or written. Written communication however is only applicable to human beings. Can you even imagine a world without communication? Verbal communication can be through telephones, webcams or in person. Written communication is through letters, emails and mobile phone messages.</p>
    <p>In today's world of great inventions and technology, letters have somehow become redundant. It is the time for text messages or chats. But they still can communicate a lot more than all other modes of communication. Organizations and various government departments still bank on letters as a strong medium of communication. There is no comparison in costs of sending letters as compared to costs of mobile phone messages though – letters are far cheaper. Letters now commonly known as "hard copy documents" are considered more relevant and important than email copies of text messages as proof or evidence of some sort.</p>
    <p>Letters speak volumes about a person or an organization that writes it. So one must take utmost care ensuring that the language used in any letter is appropriate for the occasion for which it is being written. Since a letter is also a written proof or document, if there are certain things that should not form a part of it, then that too should be carefully handled.</p>
    <p>Writing a good letter is an art. But if for some reason someone is unable to write that perfect letter, these different types of letters provide a base for you to build on. Sample letters have been given for everyone to understand what all information needs to form a part of the letter type and then it can be customized.</p>
  </div>
  <div class="signoff">Yours Sincerely,<strong>Dana Whitfield</strong></div>
  <div class="signature" role="img" aria-label="Handwritten signature"></div>
  <svg class="wave" viewBox="0 0 400 30" height="22" preserveAspectRatio="none" aria-hidden="true">
    <path d="M0 14 C120 2 260 0 400 8 L400 30 L0 30Z" fill="var(--grey-wave-light)"/>
    <path d="M0 22 C140 10 280 6 400 12 L400 30 L0 30Z" fill="var(--grey-wave)"/>
    <path d="M120 30 C200 14 300 8 400 14 L400 30Z" fill="var(--paper)" opacity=".9"/>
    <path d="M125 30 C210 16 300 12 380 30Z" fill="var(--navy)"/>
  </svg>
</section>

<section class="piece envelope-front" aria-label="Envelope front">
  <div class="brand">TM Halvorsen Law</div>
  <div class="return small">218 N. Harbor Blvd, Suite B<br>Fullerton CA 92832</div>
  <svg class="wave" viewBox="0 0 400 30" height="26" preserveAspectRatio="none" aria-hidden="true">
    <path d="M0 14 C120 2 260 0 400 8 L400 30 L0 30Z" fill="var(--grey-wave-light)"/>
    <path d="M0 22 C140 10 280 6 400 12 L400 30 L0 30Z" fill="var(--grey-wave)"/>
    <path d="M120 30 C200 14 300 8 400 14 L400 30Z" fill="var(--paper)" opacity=".9"/>
    <path d="M125 30 C210 16 300 12 380 30Z" fill="var(--navy)"/>
  </svg>
</section>

<section class="piece envelope-back" aria-label="Envelope back">
  <svg class="flap" viewBox="0 0 451 66" preserveAspectRatio="none" aria-hidden="true">
    <path d="M0 0 H451 L436 60 Q434 66 426 66 H25 Q17 66 15 60 Z" fill="var(--folder)"/>
  </svg>
  <div class="brand">TM Halvorsen Law</div>
  <div class="web small">www.tmhalvorsenlaw.com</div>
</section>

<section class="piece card-front" aria-label="Business card front">
  <div class="brand">TM Halvorsen Law</div>
</section>

<section class="piece card-back" aria-label="Business card back">
  <div class="brand">TM Halvorsen Law</div>
  <div class="divider"></div>
  <ul class="details contact">
    <li class="name">JORDAN ELLERY</li>
    <li style="margin-bottom:2px">General Manager</li>
    <li><span class="icon"></span>555.210.4180</li>
    <li><span class="icon"></span>555.210.4190</li>
    <li><span class="icon"></span>info@tmhalvorsenlaw.com</li>
    <li><span class="icon"></span>www.tmhalvorsenlaw.com</li>
    <li style="margin-top:2px">218 N. Harbor Blvd, Suite B</li>
    <li>Fullerton CA 92832</li>
  </ul>
  <svg class="wave" viewBox="0 0 400 30" height="14" preserveAspectRatio="none" aria-hidden="true">
    <path d="M0 14 C120 2 260 0 400 8 L400 30 L0 30Z" fill="var(--grey-wave-light)"/>
    <path d="M0 22 C140 10 280 6 400 12 L400 30 L0 30Z" fill="var(--grey-wave)"/>
    <path d="M120 30 C200 14 300 8 400 14 L400 30Z" fill="var(--paper)" opacity=".9"/>
    <path d="M125 30 C210 16 300 12 380 30Z" fill="var(--navy)"/>
  </svg>
</section>

</body>
</html>
```